Elegant, Playful, Health And Wellness Packaging Design for an Essential Oil Diffuser

Box design for diffuser, should be elegant, luxury, white box with gold foil and vibrant color combination that pops off the white box.

Designs look the same

```html
<!DOCTYPE html>
<html lang="en">
<head>
<meta charset="utf-8">
<title>Velmora Luma Diffuser Box</title>
<link rel="stylesheet" href="https://fonts.googleapis.com/css2?family=Mukta:wght@500;700&family=Noto+Serif:wght@400;600&family=Poppins:wght@300&display=swap">
<style>
  :root {
    --brand-blue: #0b2fbf;
    --floral-violet: #7c44e6;
    --floral-soft: #e4d8fb;
    --ink: #0d0f2e;
    --paper: #ffffff;
  }
  * { margin: 0; padding: 0; box-sizing: border-box; }
  html, body { width: 1200px; height: 738px; overflow: hidden; background: var(--paper); }
  .dieline { position: relative; width: 1200px; height: 738px; background: var(--paper); color: var(--ink); }

  /* lid flap */
  .lid { position: absolute; left: 380px; top: 84px; width: 154px; height: 160px; }
  .lid-flourish { position: absolute; left: 18px; width: 116px; height: 16px;
    background: linear-gradient(90deg, transparent, var(--ink) 20%, var(--ink) 80%, transparent); opacity: .85;
    border-radius: 8px; }
  .lid-flourish.top { top: 4px; }
  .lid-flourish.bottom { top: 138px; }
  .lid-name { position: absolute; left: 0; top: 28px; width: 154px; text-align: center;
    font: 700 26px/1 "Mukta", sans-serif; color: var(--brand-blue); transform: rotate(180deg); letter-spacing: 1px; }
  .lid-mark { position: absolute; left: 45px; top: 53px; width: 64px; height: 64px;
    border-radius: 50%; border: 5px solid var(--brand-blue); }

  /* panels */
  .panel { position: absolute; top: 305px; width: 297px; height: 238px; overflow: hidden; background: var(--paper); }
  .panel.p1 { left: 11px; } .panel.p2 { left: 308px; } .panel.p3 { left: 605px; } .panel.p4 { left: 902px; }

  .floral-top { position: absolute; right: 0; top: 0; width: 150px; height: 90px;
    background: radial-gradient(ellipse at 85% 10%, var(--floral-soft) 0%, rgba(228,216,251,.5) 45%, transparent 75%); }
  .floral-bottom { position: absolute; left: 0; bottom: 0; width: 100%; height: 120px;
    background: radial-gradient(ellipse at 30% 100%, var(--floral-soft) 0%, rgba(228,216,251,.55) 45%, transparent 80%); }
  .floral-side { position: absolute; left: 0; top: 90px; width: 50px; height: 80px;
    background: radial-gradient(ellipse at 0% 50%, var(--floral-soft), transparent 75%); }

  .tagline { position: absolute; top: 14px; left: 0; width: 100%; text-align: center;
    font: 400 9.4px/1 "Noto Serif", serif; letter-spacing: .2px; }
  .brand-mark { position: absolute; left: 117px; top: 42px; width: 64px; height: 64px;
    border-radius: 50%; border: 5px solid var(--brand-blue); }
  .brand-name { position: absolute; top: 104px; left: 0; width: 100%; text-align: center;
    font: 700 29px/1 "Mukta", sans-serif; color: var(--brand-blue); letter-spacing: 1.5px; }
  .collection { position: absolute; top: 130px; left: 0; width: 100%; text-align: center;
    font: 400 7.6px/1 "Noto Serif", serif; color: var(--floral-violet); letter-spacing: .3px; }
  .product-name { position: absolute; top: 143px; left: 146px; font: 300 58px/1 "Poppins", sans-serif;
    color: var(--brand-blue); letter-spacing: 1px; }
  .footer-line { position: absolute; top: 213px; left: 0; width: 100%; text-align: center;
    font: 400 9.2px/1 "Noto Serif", serif; }

  .info-title { position: absolute; top: 14px; left: 0; width: 100%; text-align: center;
    font: 400 10.6px/1 "Noto Serif", serif; letter-spacing: .3px; }
  .info-copy { position: absolute; top: 32px; left: 12px; width: 275px; text-align: justify;
    font: 700 7.9px/10.5px "Mukta", sans-serif; }
  .list-block { position: absolute; top: 95px; font: 700 7.9px/1 "Mukta", sans-serif; }
  .list-block.features { left: 12px; } .list-block.specs { left: 150px; }
  .list-block h3 { font: inherit; margin: 0 0 10px 18px; }
  .list-block ul { list-style: none; }
  .list-block li { height: 13.2px; padding-left: 18px; position: relative; }
  .list-block li::before { content: "★"; position: absolute; left: 2px; top: -1px; font-size: 9px; }
  .list-block li.cont { height: 13.2px; }
  .list-block li.cont::before { content: none; }
</style>
</head>
<body>
<main class="dieline">

  <section class="lid">
    <div class="lid-flourish top" role="img" aria-label="Decorative scroll flourish"></div>
    <div class="lid-name">VELMORA</div>
    <div class="lid-mark"></div>
    <div class="lid-flourish bottom" role="img" aria-label="Decorative scroll flourish"></div>
  </section>

  <section class="panel p1">
    <div class="floral-top" role="img" aria-label="Violet line illustration of roses and leaves"></div>
    <div class="floral-side" role="img" aria-label="Violet line illustration of leaves"></div>
    <div class="floral-bottom" role="img" aria-label="Violet line illustration of roses and tulips"></div>
    <div class="brand-mark"></div>
    <div class="brand-name">VELMORA</div>
    <div class="collection">SIGNATURE RARE OILS COLLECTION</div>
    <div class="product-name">LUMA</div>
    <div class="footer-line">Website url: www.velmora.com</div>
  </section>

  <section class="panel p2">
    <div class="floral-top" role="img" aria-label="Violet line illustration of roses and leaves"></div>
    <div class="floral-side" role="img" aria-label="Violet line illustration of leaves"></div>
    <div class="floral-bottom" role="img" aria-label="Violet line illustration of roses and tulips"></div>
    <div class="tagline">EXPERIENCE THE ESSENCE OF NATURE</div>
    <div class="brand-mark"></div>
    <div class="brand-name">VELMORA</div>
    <div class="collection">SIGNATURE RARE OILS COLLECTION</div>
    <div class="product-name">LUMA</div>
    <div class="footer-line">ULTRASONIC DIFFUSER</div>
  </section>

  <section class="panel p3">
    <div class="floral-top" role="img" aria-label="Soft violet line illustration of roses"></div>
    <div class="floral-bottom" role="img" aria-label="Soft violet line illustration of roses and tulips"></div>
    <div class="info-title">VELMORA RARE ESSENTIAL OILS DIFFUSER</div>
    <p class="info-copy">Experience the pure essence of nature with the Rare Oils Luma Diffuser. Sourced from the farthest reaches of the earth, Velmora Rare Oils are extracted only from the highest quality and purest raw form ingredients. Using the Luma diffuser with Velmora Rare Oils can help improve health, quality of life, and overall spiritual balance.</p>
    <div class="list-block features">
      <h3>Features :</h3>
      <ul>
        <li>Continuous diffusing</li>
        <li>Timer settings</li>
        <li>7 LED color &amp; light settings</li>
        <li>Portable</li>
        <li>Pet safe</li>
        <li>Easy to clean</li>
      </ul>
    </div>
    <div class="list-block specs">
      <h3>Specifications :</h3>
      <ul>
        <li>Dimensions : 135*135*108 mm</li>
        <li>Capacity : 300 ml</li>
        <li>33 ml / hour output</li>
        <li>Safety Auto-off when Empty</li>
        <li>Whisper Quiet</li>
        <li>Contains 1 LUMA Diffuser,</li>
        <li class="cont">1 Power Adaptor</li>
      </ul>
    </div>
  </section>

  <section class="panel p4">
    <div class="floral-top" role="img" aria-label="Violet line illustration of roses and leaves"></div>
    <div class="floral-side" role="img" aria-label="Violet line illustration of leaves"></div>
    <div class="floral-bottom" role="img" aria-label="Violet line illustration of roses and tulips"></div>
    <div class="tagline">EXPERIENCE THE ESSENCE OF NATURE</div>
    <div class="brand-mark"></div>
    <div class="brand-name">VELMORA</div>
    <div class="collection">SIGNATURE RARE OILS COLLECTION</div>
    <div class="product-name">LUMA</div>
    <div class="footer-line">ULTRASONIC DIFFUSER</div>
  </section>

</main>
</body>
</html>
```